Brochure Design Project

Trifold A4 brochure stating what we do:
Picture Framer
Fine Art Printing
Digital Press Printing
Photographer
Gallery
Studio
We have full time experienced framer
2 x Korvel 4410 large format printers
Tamsa Wrenlo Q42 Digital press printer 1st one in State of Tasmania
Will print business cards, brochures, books, postcards, etc more info available on Tamsa Wrenlo website.
Photography: Studio, Art reproduction, Wedding, Portrait,Commercial, etc.
Gallery & studio for hire

Website www.marrowlanestudio.com

The Tamsa Wrenlo Q42 printer is new addition to business. There should be more on going business for customers wanting graphic design done for printing jobs.

```html
<!DOCTYPE html>
<html lang="en">
<head>
<meta charset="utf-8">
<title>Marrow Lane Studio – Trifold Brochure</title>
<link rel="stylesheet" href="https://fonts.googleapis.com/css2?family=Cinzel:wght@400;700&family=Cinzel+Decorative:wght@700&family=Didact+Gothic&display=swap">
<style>
  :root {
    --espresso: #2a0d04;
    --walnut: #5a2714;
    --cocoa: #7a4a38;
    --tan: #c79e78;
    --sand: #dcc0a0;
    --cream: #f3e6d6;
    --ink: #4a1d0b;
    --frame: #cfa77c;
    --text-light: #f0dfcf;
  }
  * { margin: 0; padding: 0; box-sizing: border-box; }
  html, body { width: 1200px; height: 848px; overflow: hidden; background: #ffffff; }
  .brochure {
    position: relative;
    width: 1200px;
    height: 848px;
    overflow: hidden;
    font-family: "Didact Gothic", "Century Gothic", sans-serif;
    color: var(--text-light);
  }
  .backdrop { position: absolute; inset: 0; width: 1200px; height: 848px; }

  .brand-badge {
    position: absolute;
    left: 97px; top: 65px;
    width: 206px; height: 206px;
    border-radius: 50%;
    background: #ffffff;
    display: flex; align-items: center; justify-content: center;
    text-align: center;
  }
  .brand-badge__name {
    font-family: "Didact Gothic", sans-serif;
    font-size: 27px;
    line-height: 1.15;
    color: var(--ink);
    letter-spacing: 1px;
  }

  .band-title {
    position: absolute;
    top: 416px; height: 78px;
    display: flex; align-items: center; justify-content: center;
    font-family: "Cinzel Decorative", "Cinzel", serif;
    font-weight: 700;
    font-size: 27px;
    color: var(--ink);
    white-space: nowrap;
  }
  .band-title--left { left: 0; width: 400px; font-size: 25px; }
  .band-title--right { left: 802px; width: 398px; }

  .body-copy {
    position: absolute;
    font-size: 12.6px;
    line-height: 16.4px;
    text-align: justify;
    color: var(--text-light);
  }
  .body-copy--intro { left: 19px; top: 518px; width: 362px; }
  .body-copy--services { left: 826px; top: 528px; width: 356px; }

  .contact-title {
    position: absolute;
    left: 400px; width: 402px; top: 72px;
    text-align: center;
    font-family: "Cinzel", serif;
    font-weight: 700;
    font-size: 27px;
    color: var(--ink);
  }
  .contact-card {
    position: absolute;
    left: 486px; top: 216px;
    font-style: normal;
    font-size: 14.5px;
    line-height: 18px;
    color: var(--text-light);
  }
  .contact-card__name {
    font-family: "Cinzel", serif;
    font-size: 25px;
    line-height: 30px;
    color: #e9cdb6;
  }
  .contact-card__lines { margin-bottom: 40px; }
  .contact-card__web {
    position: absolute;
    left: 486px; top: 468px;
    font-style: italic;
    font-size: 15px;
    color: #e4cdbb;
  }

  .photo {
    position: absolute;
    background: var(--frame);
    padding: 9px;
  }
  .photo__image {
    width: 100%; height: 100%;
    background: linear-gradient(180deg, #2f4a78 0%, #7a5a8a 30%, #e8764a 55%, #8a6a78 72%, #3a2e30 100%);
  }
  .photo--summit { left: 916px; top: 171px; width: 207px; height: 184px; }
  .photo--dusk { left: 486px; top: 573px; width: 207px; height: 187px; }
</style>
</head>
<body>
<main class="brochure">
  <svg class="backdrop" viewBox="0 0 842 595" preserveAspectRatio="none" aria-hidden="true">
    <defs>
      <linearGradient id="panel-left" x1="0" y1="0" x2="1" y2="0">
        <stop offset="0" stop-color="#2a0d04"/>
        <stop offset="0.7" stop-color="#3c150a"/>
        <stop offset="0.85" stop-color="#6a3420"/>
        <stop offset="1" stop-color="#3a1308"/>
      </linearGradient>
      <linearGradient id="panel-mid" x1="0" y1="0" x2="1" y2="0">
        <stop offset="0" stop-color="#6e3d2a"/>
        <stop offset="0.5" stop-color="#7d4c39"/>
        <stop offset="1" stop-color="#6a3a27"/>
      </linearGradient>
      <linearGradient id="panel-right" x1="0" y1="0" x2="1" y2="0">
        <stop offset="0" stop-color="#3a1308"/>
        <stop offset="0.5" stop-color="#2a0d04"/>
        <stop offset="0.85" stop-color="#5a2816"/>
        <stop offset="1" stop-color="#3a1308"/>
      </linearGradient>
      <radialGradient id="glow" cx="0.53" cy="0.05" r="0.45">
        <stop offset="0" stop-color="#ffffff"/>
        <stop offset="0.4" stop-color="#f1e4d6"/>
        <stop offset="1" stop-color="#c99e7a"/>
      </radialGradient>
      <linearGradient id="ribbon" x1="0" y1="0" x2="1" y2="0">
        <stop offset="0" stop-color="#7a3d22"/>
        <stop offset="0.55" stop-color="#3a1307"/>
        <stop offset="1" stop-color="#b98a66"/>
      </linearGradient>
      <linearGradient id="band" x1="0" y1="0" x2="1" y2="0">
        <stop offset="0" stop-color="#c49a73"/>
        <stop offset="0.5" stop-color="#f8efe4"/>
        <stop offset="1" stop-color="#c49a73"/>
      </linearGradient>
    </defs>
    <rect x="0" y="0" width="281" height="595" fill="url(#panel-left)"/>
    <rect x="281" y="0" width="282" height="595" fill="url(#panel-mid)"/>
    <rect x="563" y="0" width="279" height="595" fill="url(#panel-right)"/>
    <line x1="281" y1="0" x2="281" y2="595" stroke="#9a6a52" stroke-width="0.8" opacity="0.6"/>
    <line x1="563" y1="0" x2="563" y2="595" stroke="#9a6a52" stroke-width="0.8" opacity="0.6"/>

    <path d="M0 0 H842 V196 C760 170 690 160 600 160 C470 160 380 70 250 62 C150 56 80 70 0 88 Z" fill="url(#ribbon)"/>
    <path d="M0 0 H842 V182 C760 158 690 146 600 148 C470 150 380 62 250 54 C150 48 80 62 0 78 Z" fill="url(#glow)"/>

    <rect x="0" y="292" width="281" height="55" fill="url(#band)"/>
    <rect x="563" y="292" width="279" height="55" fill="url(#band)"/>

    <rect x="655" y="138" width="128" height="128" fill="none" stroke="#a07055" stroke-width="3" transform="rotate(14 719 202)" opacity="0.8"/>
    <rect x="322" y="412" width="140" height="140" fill="none" stroke="#a07055" stroke-width="3" transform="rotate(12 392 482)" opacity="0.8"/>

    <circle cx="148" cy="126" r="72" fill="#d7b693"/>
  </svg>

  <div class="brand-badge">
    <span class="brand-badge__name">Marrow Lane<br>Studio</span>
  </div>

  <h2 class="band-title band-title--left">Marrow Lane Studio</h2>
  <p class="body-copy body-copy--intro">Picture framing, fine art printing, digital press printing, photography, gallery and studio hire – every part of your image, from first shot to final frame, under one roof in Tasmania.</p>

  <h1 class="contact-title">CONTACT US</h1>
  <address class="contact-card">
    <div class="contact-card__name">Dalen Ashcroft</div>
    <div class="contact-card__lines">Marrow Lane Studio<br>52 Quillan Street<br>Ferncliff, Tasmania 7010</div>
    <div>Phone : 03 5550 1842<br>Mobile : 0400 555 219<br>eMail : hello@marrowlanestudio.com</div>
  </address>
  <div class="contact-card__web">http://www.marrowlanestudio.com</div>

  <h2 class="band-title band-title--right">What We Do</h2>
  <p class="body-copy body-copy--services">Marrow Lane Studio is a picture framer, fine art printer, digital press printer, photographer, gallery and studio in one. Our full time experienced framer builds custom frames for artwork, photographs, certificates and keepsakes. Two Korvel 4410 large format printers produce gallery quality fine art prints on archival papers and canvas. Our newest addition, the Tamsa Wrenlo Q42 digital press, is the first one in the State of Tasmania. It prints business cards, brochures, books, postcards and much more, with further details on the Tamsa Wrenlo website. Need artwork for your print job? Our graphic design service prepares layouts and files ready for press. Photography covers studio sessions, art reproduction, weddings, portraits and commercial work, with every image printed and framed in house. The gallery and studio are also available for hire for exhibitions, launches, workshops and photo shoots. Call in, talk to our team and see what we can make for you.</p>

  <figure class="photo photo--summit">
    <div class="photo__image" role="img" aria-label="Photograph of a rocky mountain summit silhouetted against a vivid sunset sky above clouds"></div>
  </figure>
  <figure class="photo photo--dusk">
    <div class="photo__image" role="img" aria-label="Photograph of rock formations on a ridge at dusk with an orange and pink sunset over low cloud"></div>
  </figure>
</main>
</body>
</html>
```